Business Card Design with new logo

Warren Peltzman 4175
E 118th Rd Dunmore Falls, IL 62999
Cell: 217-555-0187
peltzmanrebuilds@mailhollow.com

Classic Car Restoration Services Buy Sell Trade Consign

Contact Information for Business Card

Warren Peltzman 9698
Cell: 217-555-0187

```html
<!DOCTYPE html>
<html lang="en">
<head>
<meta charset="utf-8">
<title>Ironvale Restoration LLC – Business Card</title>
<link rel="stylesheet" href="https://fonts.googleapis.com/css2?family=Roboto+Condensed:wght@300;400;700&display=swap">
<style>
  :root {
    --stage: #2a2c2e;
    --navy: #14232e;
    --navy-light: #22333f;
    --white: #ffffff;
    --red: #e63b3b;
  }
  * { box-sizing: border-box; margin: 0; padding: 0; }
  html, body { width: 1200px; height: 896px; overflow: hidden; background: var(--stage); }
  body {
    font-family: "Roboto Condensed", Arial, sans-serif;
    display: flex; flex-direction: column; align-items: center; justify-content: center; gap: 56px;
  }
  .card {
    width: 560px; height: 320px; border-radius: 22px; overflow: hidden; position: relative;
    box-shadow: 0 18px 40px rgba(0,0,0,.45);
  }
  /* Front */
  .card-front {
    background: linear-gradient(135deg, var(--navy-light), var(--navy) 60%);
    display: flex; flex-direction: column; align-items: center; justify-content: center; gap: 14px;
  }
  .brand { display: flex; align-items: center; gap: 14px; }
  .brand-dot { width: 26px; height: 26px; border-radius: 50%; background: var(--red); }
  .brand-name {
    font-weight: 700; font-size: 46px; letter-spacing: 2px; color: var(--white); text-transform: uppercase;
  }
  .brand-sub {
    font-weight: 400; font-size: 17px; letter-spacing: 9px; color: var(--white); text-transform: uppercase;
  }
  /* Back */
  .card-back { background: var(--white); }
  .back-dark {
    position: absolute; left: 0; right: 0; bottom: 0; height: 44%;
    background: linear-gradient(90deg, var(--navy-light), var(--navy));
  }
  .back-brand {
    position: absolute; left: 34px; top: 60px; display: flex; flex-direction: column; gap: 6px;
  }
  .back-brand .brand-name { color: var(--navy); font-size: 30px; letter-spacing: 1px; }
  .back-brand .brand-sub { color: var(--red); font-size: 11px; letter-spacing: 6px; }
  .person { position: absolute; right: 36px; top: 48px; text-align: right; }
  .person-name { color: var(--red); font-size: 30px; font-weight: 400; text-transform: uppercase; }
  .person-title { color: var(--navy); font-size: 14px; font-weight: 300; }
  .contacts {
    position: absolute; left: 34px; bottom: 22px; list-style: none;
    color: var(--white); font-size: 14px; font-weight: 300; display: flex; flex-direction: column; gap: 5px;
  }
  .contacts li { display: flex; align-items: center; gap: 8px; }
  .contacts svg { width: 12px; height: 12px; fill: none; stroke: var(--white); stroke-width: 1.6; }
  .address {
    position: absolute; right: 36px; bottom: 40px; text-align: right;
    color: var(--white); font-size: 14px; font-weight: 300; line-height: 1.4;
  }
</style>
</head>
<body>
  <section class="card card-front">
    <div class="brand">
      <span class="brand-dot"></span>
      <span class="brand-name">Ironvale</span>
    </div>
    <span class="brand-sub">Restoration LLC</span>
  </section>

  <section class="card card-back">
    <div class="back-dark"></div>
    <div class="back-brand">
      <span class="brand-name">Ironvale</span>
      <span class="brand-sub">Restoration LLC</span>
    </div>
    <div class="person">
      <p class="person-name">Dorian Vance</p>
      <p class="person-title">Director</p>
    </div>
    <ul class="contacts">
      <li><svg viewBox="0 0 12 12"><path d="M3 1l2 2.5-1.2 1.2a7 7 0 0 0 3.5 3.5L8.5 7 11 9l-1.5 2C5 11 1 7 1 2.5z"/></svg>217-555-0187</li>
      <li><svg viewBox="0 0 12 12"><rect x="1" y="2.5" width="10" height="7" rx="1"/><path d="M1 3l5 4 5-4"/></svg>peltzmanrebuilds@mailhollow.com</li>
      <li><svg viewBox="0 0 12 12"><circle cx="6" cy="6" r="5"/><path d="M1 6h10M6 1c2 2.5 2 7.5 0 10M6 1c-2 2.5-2 7.5 0 10"/></svg>www.ironvalerebuilds.com</li>
    </ul>
    <p class="address">Warren Peltzman 4175<br>E 118th Rd Dunmore Falls, IL 62999</p>
  </section>
</body>
</html>
```